International School Business Card Design

We need a new business card design for our Houston, Texas based international school, The Marlowe School. Our school features an extremely low student-teacher ratio, making it among the most expensive schools in Houston. Design should reflect a school/business at the high end of the market. Designs should incorporate our current school logo.

Target Market(s)

Card should appeal to potential parents/customers of our international private school.

Industry/Entity Type

Education

Contact Information for Business Card

The Marlowe School
4120 North Pembry Rd | Houston, Texas 77418

Daniel R. Marlowe
Head of School
www.marloweschool-example.com
dmarlowe@marloweschool-example.com
(713) 555-0148

Requirements
Must have
• Business card details and school logo

```html
<!DOCTYPE html>
<html lang="en">
<head>
<meta charset="utf-8">
<title>The Marlowe School – Business Card</title>
<link rel="stylesheet" href="https://fonts.googleapis.com/css2?family=Arimo:wght@400;700&display=swap">
<style>
  :root {
    --backdrop: #2b2b2b;
    --card: #ffffff;
    --navy: #1d3f8f;
    --ink: #4a4a4a;
    --rule: #c9c9c9;
    --green: #8cc63f;
    --gold: #b8901c;
  }
  * { box-sizing: border-box; margin: 0; padding: 0; }
  html, body {
    width: 1200px; height: 1063px; overflow: hidden;
    background: var(--backdrop);
    font-family: "Arimo", Arial, sans-serif;
  }
  .card {
    position: absolute; left: 75px; top: 231px;
    width: 1050px; height: 600px;
    background: var(--card);
    box-shadow: 0 18px 40px rgba(0,0,0,.45);
    overflow: hidden;
  }
  .holder { position: absolute; left: 64px; top: 150px; }
  .holder-name { color: var(--navy); font-weight: 700; font-size: 30px; letter-spacing: .2px; }
  .holder-title { color: var(--ink); font-size: 21px; margin-top: 6px; }

  .contact { position: absolute; left: 600px; top: 190px; width: 400px; }
  .school-name { color: var(--navy); font-weight: 700; font-size: 22px; }
  .address { color: var(--ink); font-size: 20px; line-height: 1.28; margin-top: 4px; }
  .divider { height: 1px; background: var(--rule); margin: 14px 0 12px; }
  .lines { list-style: none; }
  .lines li {
    display: flex; align-items: center; gap: 12px;
    color: var(--ink); font-size: 19px; line-height: 1.45;
  }
  .lines svg { width: 18px; height: 18px; flex: none; fill: var(--gold); }

  .wordmark {
    position: absolute; left: 64px; top: 430px;
    display: flex; align-items: center; gap: 14px;
  }
  .wordmark-dot { width: 54px; height: 54px; border-radius: 50%; background: var(--navy); }
  .wordmark-name { color: var(--navy); font-weight: 700; font-size: 36px; }

  .band {
    position: absolute; left: 0; right: 0; bottom: 0; height: 44px;
    background: var(--green);
  }
</style>
</head>
<body>
  <div class="card">
    <div class="holder">
      <div class="holder-name">Daniel R. Marlowe</div>
      <div class="holder-title">Head of School</div>
    </div>

    <div class="contact">
      <div class="school-name">The Marlowe School</div>
      <div class="address">4120 North Pembry Rd<br>Houston, Texas 77418</div>
      <div class="divider"></div>
      <ul class="lines">
        <li>
          <svg viewBox="0 0 24 24" aria-hidden="true"><path d="M6.6 10.8a15.1 15.1 0 0 0 6.6 6.6l2.2-2.2c.3-.3.7-.4 1-.2 1.1.4 2.3.6 3.6.6.6 0 1 .4 1 1V20c0 .6-.4 1-1 1A17 17 0 0 1 3 4c0-.6.4-1 1-1h3.5c.6 0 1 .4 1 1 0 1.3.2 2.5.6 3.6.1.3 0 .7-.2 1z"/></svg>
          (713) 555-0148
        </li>
        <li>
          <svg viewBox="0 0 24 24" aria-hidden="true"><path d="M12 2a10 10 0 1 0 0 20 10 10 0 0 0 0-20zm6.9 6h-2.9a15.7 15.7 0 0 0-1.4-3.6A8 8 0 0 1 18.9 8zM12 4c.8 1.2 1.5 2.5 1.9 4h-3.8c.4-1.5 1.1-2.8 1.9-4zM4.3 14a8.2 8.2 0 0 1 0-4h3.4a16.5 16.5 0 0 0 0 4zm.8 2h2.9c.3 1.3.8 2.5 1.4 3.6A8 8 0 0 1 5.1 16zM8 8H5.1a8 8 0 0 1 4.3-3.6C8.8 5.5 8.3 6.7 8 8zm4 12c-.8-1.2-1.5-2.5-1.9-4h3.8c-.4 1.5-1.1 2.8-1.9 4zm2.3-6H9.7a14.7 14.7 0 0 1 0-4h4.6a14.7 14.7 0 0 1 0 4zm.3 5.6c.6-1.1 1.1-2.3 1.4-3.6h2.9a8 8 0 0 1-4.3 3.6zm1.7-5.6a16.5 16.5 0 0 0 0-4h3.4a8.2 8.2 0 0 1 0 4z"/></svg>
          www.marloweschool-example.com
        </li>
        <li>
          <svg viewBox="0 0 24 24" aria-hidden="true"><path d="M3 5h18c.6 0 1 .4 1 1v12c0 .6-.4 1-1 1H3c-.6 0-1-.4-1-1V6c0-.6.4-1 1-1zm9 7.2L4.4 7v.1L12 12l7.6-5V7z"/></svg>
          dmarlowe@marloweschool-example.com
        </li>
      </ul>
    </div>

    <div class="wordmark">
      <span class="wordmark-dot"></span>
      <span class="wordmark-name">The Marlowe School</span>
    </div>

    <div class="band"></div>
  </div>
</body>
</html>
```